Marlowick APP redesign and color change

I am looking for a new design for my app. Please see the attached current design.

Currently, I have a functioning app but the colors and design are awful!
The logo is great but the rest of the app needs a refresh.
(Logo hi res not yet available but will upload soon.)
New colors or anything that is cutting edge.

Basically: It is a secure social media app within a school system where the teachers, students and parents can text, exchange photos, plan curriculum, etc.

I NEED ONLY landing page with a new look!
Looking for one distinct design for the landing page with new look.
The developer will apply this one design towards the rest of the pages/app screens.

Because part of the social media I need the feel and look of what is now the trend. Something that will attract and keep the client(s) interested. I am really leaving all the creative work to the designer and open to any suggestions.
Updates

Target Market(s)

Schools, community, teachers, students, colleges, sport teams

Industry/Entity Type

Non Profit

Font styles to use
Serif
Sans Serif

Colors

Designer to choose colors to be used in the design.

Requirements
Must have
• Sharp, trendy, millennial feel
Nice to have
• Up to designer
Should not have
• Up to designer

```html
<!DOCTYPE html>
<html lang="en">
<head>
<meta charset="utf-8">
<title>Marlowick App Screens</title>
<link href="https://fonts.googleapis.com/css2?family=Lato:wght@300;400;700&display=swap" rel="stylesheet">
<style>
  :root {
    --stage: #2a2823;
    --white: #ffffff;
    --leaf-dark: #2f4d12;
    --leaf-mid: #5f8a22;
    --leaf-light: #b9cf4a;
    --leaf-pale: #dfe59a;
    --olive-bar: #7f8c1c;
    --field-fill: rgba(255,255,255,0.22);
    --field-line: rgba(255,255,255,0.85);
    --list-bg: #f3f4f4;
    --row-line: #3d4a52;
    --ink: #2d2d2d;
    --chevron: #3c5a6e;
    --avatar-a: #5a6f86;
    --avatar-b: #9a9a96;
  }
  * { box-sizing: border-box; margin: 0; padding: 0; }
  html, body { width: 1200px; height: 832px; overflow: hidden; }
  body {
    background: var(--stage);
    font-family: "Lato", sans-serif;
    color: var(--white);
    position: relative;
  }
  .screen {
    position: absolute;
    top: 28px;
    width: 440px;
    height: 776px;
    overflow: hidden;
  }
  .screen--login { left: 120px; }
  .screen--conversation { left: 640px; background: var(--list-bg); }

  .foliage {
    position: absolute; inset: 0;
    background:
      radial-gradient(ellipse 60% 30% at 70% 12%, rgba(200,220,90,0.55), transparent 70%),
      radial-gradient(ellipse 50% 35% at 20% 40%, rgba(40,70,15,0.7), transparent 70%),
      radial-gradient(ellipse 70% 40% at 50% 90%, rgba(220,225,120,0.8), transparent 70%),
      linear-gradient(180deg, var(--leaf-mid) 0%, var(--leaf-dark) 35%, var(--leaf-mid) 60%, var(--leaf-light) 85%, var(--leaf-pale) 100%);
  }

  .status-bar {
    position: absolute; top: 0; left: 0; right: 0; height: 24px;
    display: flex; align-items: center; justify-content: space-between;
    padding: 0 10px; font-size: 14px; font-weight: 400;
  }
  .status-bar .signal { letter-spacing: 1px; }
  .status-bar .time { position: absolute; left: 50%; transform: translateX(-50%); }

  .brand {
    position: absolute; top: 190px; left: 0; right: 0; text-align: center;
  }
  .brand__dot {
    width: 130px; height: 130px; border: 3px solid var(--white); border-radius: 50%;
    margin: 0 auto 20px;
  }
  .brand__name {
    font-size: 21px; font-weight: 700; letter-spacing: 9px; padding-left: 9px; line-height: 25px;
  }
  .brand__tagline {
    margin-top: 6px; font-size: 11px; font-weight: 300; letter-spacing: 0.6px;
  }

  .login-form { position: absolute; top: 439px; left: 61px; }
  .field { display: flex; align-items: center; margin-bottom: 7px; }
  .field__icon {
    width: 33px; height: 33px; border: 2px solid var(--white); border-radius: 50%;
    display: flex; align-items: center; justify-content: center; margin-right: 12px;
  }
  .field__box {
    width: 256px; height: 40px; background: var(--field-fill);
    border: 1px solid var(--field-line);
    display: flex; align-items: center; justify-content: space-between;
    padding: 0 12px 0 14px; font-size: 18px; font-weight: 300;
  }

  .login-footer {
    position: absolute; left: 0; right: 0; bottom: 0; height: 36px;
    background: var(--olive-bar);
    display: flex; align-items: center; justify-content: space-between;
    padding: 0 16px; font-size: 16px; font-weight: 300;
  }

  .convo-header { position: absolute; top: 0; left: 0; right: 0; height: 126px; overflow: hidden; }
  .convo-header .foliage {
    background:
      radial-gradient(ellipse 40% 60% at 75% 30%, rgba(190,215,80,0.6), transparent 70%),
      linear-gradient(180deg, var(--leaf-dark), var(--leaf-mid) 70%, var(--leaf-light));
  }
  .convo-header__title {
    position: absolute; top: 36px; left: 0; right: 0; text-align: center;
    font-size: 21px; font-weight: 400; letter-spacing: 1.5px;
  }
  .search {
    position: absolute; top: 85px; left: 8px; right: 7px; height: 32px;
    border: 1.5px solid var(--white); background: rgba(255,255,255,0.2);
    display: flex; align-items: center; padding-left: 8px;
  }

  .thread-list { position: absolute; top: 144px; left: 10px; right: 10px; border-top: 1.5px solid var(--row-line); list-style: none; }
  .thread {
    height: 94px; border-bottom: 1.5px solid var(--row-line);
    display: flex; align-items: center; padding-left: 3px; color: var(--ink);
  }
  .thread__avatar { width: 55px; height: 55px; border-radius: 50%; background: var(--avatar-a); margin-right: 13px; flex: none; }
  .thread__avatar--alt { background: var(--avatar-b); }
  .thread__text { flex: 1; }
  .thread__name { font-size: 16px; font-weight: 700; margin-bottom: 6px; }
  .thread__preview { font-size: 18px; font-weight: 400; }
  .thread__chevron { margin-right: 14px; }

  .tab-bar {
    position: absolute; left: 0; right: 0; bottom: 0; height: 60px;
    background: linear-gradient(90deg, var(--olive-bar), var(--leaf-light) 60%, var(--olive-bar));
    display: flex;
  }
  .tab { flex: 1; display: flex; align-items: center; justify-content: center; }
  .tab--active { background: rgba(80,95,15,0.55); }
</style>
</head>
<body>

<section class="screen screen--login">
  <div class="foliage" role="img" aria-label="Soft blurred photograph of sunlit green foliage"></div>

  <div class="status-bar">
    <span class="signal">●●●○○ Nexa</span>
    <span class="time">8:19 AM</span>
    <span>50% ▭</span>
  </div>

  <div class="brand">
    <div class="brand__dot"></div>
    <div class="brand__name">MARLOWICK</div>
    <div class="brand__tagline">CONNECTED THROUGH COMMUNITY</div>
  </div>

  <form class="login-form">
    <div class="field">
      <span class="field__icon">
        <svg width="16" height="12" viewBox="0 0 16 12"><rect x="0.5" y="0.5" width="15" height="11" fill="#fff"/><path d="M1 1l7 6 7-6" fill="none" stroke="#5f8a22" stroke-width="1.4"/></svg>
      </span>
      <span class="field__box">name@inbox.example</span>
    </div>
    <div class="field">
      <span class="field__icon">
        <svg width="14" height="17" viewBox="0 0 14 17"><path d="M3.5 7V4.5a3.5 3.5 0 0 1 7 0V7" fill="none" stroke="#fff" stroke-width="2"/><rect x="1" y="7" width="12" height="9.5" rx="1" fill="#fff"/></svg>
      </span>
      <span class="field__box">pin
        <svg width="26" height="18" viewBox="0 0 26 18"><path d="M1 9c4-6 20-6 24 0-4 6-20 6-24 0z" fill="none" stroke="#fff" stroke-width="1.5"/><circle cx="13" cy="9" r="3.5" fill="none" stroke="#fff" stroke-width="1.5"/><path d="M4 17L22 1" stroke="#fff" stroke-width="1.5"/></svg>
      </span>
    </div>
  </form>

  <footer class="login-footer">
    <span>Sign Up for Marlowick</span>
    <span>Forgot your password?</span>
  </footer>
</section>

<section class="screen screen--conversation">
  <header class="convo-header">
    <div class="foliage" role="img" aria-label="Blurred green foliage photograph as header backdrop"></div>
    <div class="status-bar">
      <span class="signal">●●●○○ Nexa</span>
      <span class="time">8:19 AM</span>
      <span>50% ▭</span>
    </div>
    <h1 class="convo-header__title">CONVERSATION</h1>
    <div class="search">
      <svg width="18" height="18" viewBox="0 0 18 18"><circle cx="7.5" cy="7.5" r="5.5" fill="none" stroke="#fff" stroke-width="2"/><path d="M11.5 11.5L16.5 16.5" stroke="#fff" stroke-width="2.2"/></svg>
    </div>
  </header>

  <ul class="thread-list">
    <li class="thread"><span class="thread__avatar" role="img" aria-label="Contact profile photo"></span><div class="thread__text"><div class="thread__name">Lorem Ipsum</div><div class="thread__preview">Lorem Ipsum dolor sit amet</div></div><svg class="thread__chevron" width="12" height="22" viewBox="0 0 12 22"><path d="M1 1l10 10L1 21" fill="none" stroke="#3c5a6e" stroke-width="2.2"/></svg></li>
    <li class="thread"><span class="thread__avatar thread__avatar--alt" role="img" aria-label="Contact profile photo"></span><div class="thread__text"><div class="thread__name">Lorem Ipsum</div><div class="thread__preview">Lorem Ipsum dolor sit amet</div></div><svg class="thread__chevron" width="12" height="22" viewBox="0 0 12 22"><path d="M1 1l10 10L1 21" fill="none" stroke="#3c5a6e" stroke-width="2.2"/></svg></li>
    <li class="thread"><span class="thread__avatar" role="img" aria-label="Contact profile photo"></span><div class="thread__text"><div class="thread__name">Lorem Ipsum</div><div class="thread__preview">Lorem Ipsum dolor sit amet</div></div><svg class="thread__chevron" width="12" height="22" viewBox="0 0 12 22"><path d="M1 1l10 10L1 21" fill="none" stroke="#3c5a6e" stroke-width="2.2"/></svg></li>
    <li class="thread"><span class="thread__avatar thread__avatar--alt" role="img" aria-label="Contact profile photo"></span><div class="thread__text"><div class="thread__name">Lorem Ipsum</div><div class="thread__preview">Lorem Ipsum dolor sit amet</div></div><svg class="thread__chevron" width="12" height="22" viewBox="0 0 12 22"><path d="M1 1l10 10L1 21" fill="none" stroke="#3c5a6e" stroke-width="2.2"/></svg></li>
    <li class="thread"><span class="thread__avatar" role="img" aria-label="Contact profile photo"></span><div class="thread__text"><div class="thread__name">Lorem Ipsum</div><div class="thread__preview">Lorem Ipsum dolor sit amet</div></div><svg class="thread__chevron" width="12" height="22" viewBox="0 0 12 22"><path d="M1 1l10 10L1 21" fill="none" stroke="#3c5a6e" stroke-width="2.2"/></svg></li>
    <li class="thread"><span class="thread__avatar thread__avatar--alt" role="img" aria-label="Contact profile photo"></span><div class="thread__text"><div class="thread__name">Lorem Ipsum</div><div class="thread__preview">Lorem Ipsum dolor sit amet</div></div><svg class="thread__chevron" width="12" height="22" viewBox="0 0 12 22"><path d="M1 1l10 10L1 21" fill="none" stroke="#3c5a6e" stroke-width="2.2"/></svg></li>
  </ul>

  <nav class="tab-bar">
    <span class="tab tab--active"><svg width="28" height="26" viewBox="0 0 28 26"><rect x="7" y="2" width="19" height="15" fill="none" stroke="#fff" stroke-width="1.8"/><path d="M2 7v14h4v4l4-4h10" fill="none" stroke="#fff" stroke-width="1.8"/></svg></span>
    <span class="tab"><svg width="26" height="26" viewBox="0 0 26 26" fill="none" stroke="#fff" stroke-width="1.8"><rect x="2" y="2" width="9" height="9"/><rect x="15" y="2" width="9" height="9"/><rect x="2" y="15" width="9" height="9"/><rect x="15" y="15" width="9" height="9"/></svg></span>
    <span class="tab"><svg width="22" height="26" viewBox="0 0 22 26" fill="none" stroke="#fff" stroke-width="1.8"><rect x="3" y="1" width="17" height="24" rx="1"/><circle cx="11.5" cy="10" r="3"/><path d="M6.5 19c1-4 9-4 10 0"/><path d="M1 6h3M1 12h3M1 18h3"/></svg></span>
    <span class="tab"><svg width="26" height="26" viewBox="0 0 26 26" fill="none" stroke="#fff" stroke-width="1.8"><circle cx="13" cy="13" r="4"/><path d="M13 2v3M13 21v3M2 13h3M21 13h3M5.2 5.2l2.1 2.1M18.7 18.7l2.1 2.1M5.2 20.8l2.1-2.1M18.7 7.3l2.1-2.1"/><circle cx="13" cy="13" r="8"/></svg></span>
  </nav>
</section>

</body>
</html>
```